Gift card design to reflect the theme from our overhead business sign

We need a gift card that aligns with our colors used for the sign. Since I am not sure what you're able to do with the limited space, if you think you can create a miniature version of the sign and add the words "Gift Card" to it. I'd like to see it. I have also uploaded the original logo we use as an other variable to use in place the horizontal one on the sign. That might be alright too. Give me a few options to consider.

Then for the back of the card there may be some legal requirements for the wording. I'll get back to you on that. First, let's focus on the design.

Also, i am sending the requirements for "Quorix" who will be the processor for the card. I will be doing custom cards so pay attention to page 4.

After the gift card, I will sending you the front of the store image with the sign in place, so you can come up with some ideas for a simple window design to go across all the windows.

How fast can you get back to me? Unlike the sign, I'm sort of in a time crunch.

Oh, one other thing, I want to change the pink in our current logo to the pink you used in the sign. So if you use our standard logo, please change the pink to the on you used for the sign.

```html
<!DOCTYPE html>
<html lang="en">
<head>
<meta charset="utf-8">
<title>Sweet Loft Bakery Gift Card</title>
<link rel="stylesheet" href="https://fonts.googleapis.com/css2?family=Fredoka:wght@600;700&display=swap">
<style>
  :root {
    --pink: #ec3c94;
    --green: #afd34a;
    --green-dark: #6e8a22;
    --green-edge: #5e7a1a;
    --white: #ffffff;
  }
  html, body {
    margin: 0;
    padding: 0;
    width: 1200px;
    height: 785px;
    overflow: hidden;
    background: var(--white);
  }
  .gift-card {
    position: relative;
    width: 1200px;
    height: 785px;
    overflow: hidden;
    font-family: "Fredoka", sans-serif;
  }
  .card-backdrop {
    position: absolute;
    inset: 0;
    width: 1200px;
    height: 785px;
  }
  .brand-name {
    position: absolute;
    left: 0;
    right: 0;
    top: 148px;
    margin: 0;
    text-align: center;
    font-weight: 700;
    font-size: 112px;
    line-height: 1;
    letter-spacing: 1px;
    color: var(--white);
  }
  .brand-tagline {
    position: absolute;
    right: 185px;
    top: 282px;
    margin: 0;
    font-weight: 700;
    font-size: 50px;
    line-height: 1;
    color: var(--white);
  }
  .card-label {
    position: absolute;
    left: 0;
    right: 0;
    top: 548px;
    margin: 0;
    text-align: center;
    font-weight: 700;
    font-size: 128px;
    line-height: 1;
    letter-spacing: 2px;
    color: var(--white);
    -webkit-text-stroke: 10px var(--green-edge);
    paint-order: stroke fill;
    text-shadow: 14px 16px 0 var(--green-dark);
  }
</style>
</head>
<body>
  <main class="gift-card">
    <svg class="card-backdrop" viewBox="0 0 1088 712" preserveAspectRatio="none" aria-hidden="true">
      <rect class="lower-field" x="0" y="0" width="1088" height="712" fill="var(--green)"/>
      <polygon class="upper-flap" points="0,0 1088,0 1088,283 745,440 543,358 340,440 0,283" fill="var(--pink)"/>
      <polygon class="flap-edge-left" points="0,283 340,440 340,456 0,300" fill="var(--white)"/>
      <polygon class="flap-edge-right" points="1088,283 745,440 745,456 1088,300" fill="var(--white)"/>
      <polygon class="center-chevron" points="100,545 543,358 985,545 543,378" fill="var(--white)"/>
    </svg>

    <h1 class="brand-name">Sweet Loft Bakery</h1>
    <p class="brand-tagline">fresh bakes to go</p>
    <p class="card-label">Gift Card</p>
  </main>
</body>
</html>
```